Professional and modern website for Real Estate services company

Hi there! We're looking for a responsive, highly professional and modern (in line with Latest trends) coded website for a Real Estate services company named Portalia720º (find logo attached). I will try to Explain how I picture it in my head, but feel free to step out of the script and design it as you please. The structure for the website must be as Follows: - Menu: at the top of the screen, always visible (in any page and when to scrolling down). Logo at the left hand side (clicking redirects to home), then a Services, About us, Blog and Contact and on the right hand, Estimate and Log in (just placeholder, no log in required yet). - Home: (I like https://fr.domvera.example/): a landscape picture of Madrid's skyline. Very important That at a first glance (without scrolling) you can see a box to input data of your building to get an estimate (Post code, Number of homes, Number of garages, Number of stores, Swimming pool (yes / no) Concierge (yes / no)). Should there be a small space Also for a corporate presentation video (more or less like https://www.velbrastahogares.example/ but With the estimate Request box INSTEAD OF the App - however, do not take this one as example Given I just wanted to illustrate the structure). Still in the Home, bellow the first glance, I'd like to have a brief introduction of the following pages (Services, About us, Blog and Contact). This can be in a Either "square" form (like https://fr.domvera.example/) or in a "scroll" form (like https://k7pisos.example/). - Services: we offer 3 sets of services, each of them composed by three specific services, Namely: * Administration Treasury Accounting Savings * Consulting Legal Technical Regulatory * Mediation Repairs Meetings Delinquency For the sake of structuring, each of the nine services will Have to written description composed of 3 small paragraphs of About 15 words. I Tend to like to Accompany With each of the services related icons / vectors, but feel free to design them as you want. - About us: content not yet defined, but will be a series of bullets / sections in Which We talk about prep or differentiating points. We can include the corporate video presentation here again. - Blog: just a space Where you can see to the blog entries (in Home, probably just show 3/4). - Contact: a fancy contact form, with map, address, telephone, e-mail and opening hours. Just to give it a bit more content, maybe include a catch phrase like "We're looking forward to meeting you!" or something like that. - Estimate: this is the Most Important page in the website (in Addition to the upper part of the Home page). Basically replicate the estimate for the home box, but maybe with a bit more design or extended, Given this is a single page just for that. - Log in: opens a drop-down with user and password (just placeholder, no log in required yet). Regarding colors, we still do not Have a color scheme, so anything in line With the logo is OK. Many thanks in advance, Martin

All ages and genders

Real Estate

Coded - Design and coding required

5+ page

Sans Serif

Must have
• Blank colored background

```html
<!DOCTYPE html>
<html lang="en">
<head>
<meta charset="utf-8">
<title>Portalia720º — Real Estate Services</title>
<link rel="stylesheet" href="https://fonts.googleapis.com/css2?family=Open+Sans:wght@400;600;700&family=Raleway:wght@600;700;800&display=swap">
<style>
  :root {
    --orange: #ef7d0a;
    --orange-dark: #d96f05;
    --ink: #1c1c1c;
    --text: #444;
    --muted: #777;
    --grey-btn: #4a4a4a;
    --light: #ececec;
    --footer: #2b2b2b;
    --footer-bottom: #1f1f1f;
    --footer-text: #c8c8c8;
    --white: #fff;
    --line: #cfcfcf;
  }
  * { box-sizing: border-box; margin: 0; padding: 0; }
  html, body { width: 1200px; height: 2961px; overflow: hidden; }
  body { font-family: "Open Sans", Arial, sans-serif; color: var(--text); background: var(--white); position: relative; }
  .abs { position: absolute; }

  /* Header */
  .site-header { position: absolute; left: 0; top: 0; width: 1200px; height: 122px; background: var(--white); }
  .brand { left: 64px; top: 40px; font-family: "Open Sans", sans-serif; font-weight: 700; font-size: 38px; color: #555; display: flex; align-items: center; gap: 10px; }
  .brand-mark { width: 14px; height: 14px; background: var(--orange); }
  .top-mail { left: 642px; top: 9px; font-size: 15px; color: #333; display: flex; align-items: center; gap: 8px; font-weight: 600; }
  .top-phone { left: 922px; top: 2px; width: 136px; height: 34px; background: var(--orange); color: var(--white); font-size: 15px; display: flex; align-items: center; justify-content: center; gap: 8px; }
  .social { top: 6px; width: 28px; height: 28px; border-radius: 50%; }
  .social.one { left: 1070px; background: #3b5a98; }
  .social.two { left: 1102px; background: #2aa7e0; }
  .main-nav { left: 543px; top: 74px; display: flex; height: 46px; }
  .main-nav a { display: flex; align-items: center; padding: 0 12px; margin-right: 18px; font-size: 15px; font-weight: 700; color: #222; text-decoration: none; }
  .main-nav a:last-child { margin-right: 0; }
  .main-nav a.active { background: var(--orange); color: var(--white); }

  /* Hero */
  .hero { position: absolute; left: 0; top: 122px; width: 1200px; height: 612px; }
  .hero-photo { position: absolute; inset: 0; background: linear-gradient(180deg, #d9d6cf 0%, #b8b7b2 22%, #7c8085 55%, #5b5f63 100%); }
  .estimate-band { position: absolute; left: 63px; top: 474px; width: 1137px; height: 138px; background: var(--orange); }
  .estimate-band h2 { position: absolute; left: 22px; top: 12px; color: var(--white); font-weight: 400; font-size: 25px; }
  .estimate-form { position: absolute; left: 12px; top: 64px; display: flex; align-items: center; }
  .search-icon { width: 50px; height: 50px; margin-right: 10px; }
  .estimate-form .field { height: 50px; background: var(--white); border-right: 1px solid #ddd; font-size: 13px; color: #999; display: flex; align-items: center; padding-left: 11px; }
  .estimate-form .submit { width: 134px; height: 50px; background: #0d0d0d; color: var(--white); font-size: 21px; font-weight: 600; display: flex; align-items: center; justify-content: center; margin-left: 2px; }

  /* Provide */
  .provide-title { left: 0; top: 806px; width: 1200px; text-align: center; font-family: "Raleway", sans-serif; font-weight: 800; font-size: 41px; color: #111; }
  .provide-lead { left: 250px; top: 874px; width: 700px; text-align: center; font-size: 13.5px; line-height: 24px; color: #444; }
  .service-card { top: 979px; width: 296px; height: 423px; background: #f6f6f6; }
  .service-card h3 { height: 51px; background: var(--orange); color: var(--white); font-family: "Raleway", sans-serif; font-size: 22px; font-weight: 700; text-align: center; line-height: 51px; }
  .service-photo { height: 198px; }
  .service-card p { padding: 10px 14px 0; font-size: 13.5px; line-height: 20.5px; text-align: center; color: #555; height: 124px; }
  .card-btn { margin: 0 4px; height: 48px; background: var(--grey-btn); color: var(--white); font-size: 16px; font-weight: 600; display: flex; align-items: center; justify-content: center; gap: 10px; box-shadow: 0 6px 8px -4px rgba(0,0,0,.35); }

  /* News band */
  .news { position: absolute; left: 0; top: 1494px; width: 1200px; height: 510px; background: var(--orange); overflow: hidden; }
  .news h2 { position: absolute; left: 64px; top: 60px; width: 1000px; color: var(--white); font-family: "Raleway", sans-serif; font-size: 30px; font-weight: 700; line-height: 36px; }
  .tablet { position: absolute; left: 24px; top: 184px; width: 722px; height: 340px; }
  .news-copy { position: absolute; left: 756px; top: 176px; width: 430px; color: var(--white); font-size: 13.5px; line-height: 21.5px; }
  .news-btn { position: absolute; left: 756px; top: 395px; width: 239px; height: 48px; background: var(--grey-btn); color: var(--white); font-size: 16px; font-weight: 600; display: flex; align-items: center; justify-content: center; }

  /* Contact */
  .contact { position: absolute; left: 0; top: 2004px; width: 1200px; height: 487px; background: var(--light); }
  .contact-box { position: absolute; left: 63px; top: 69px; width: 1076px; height: 339px; background: var(--white); }
  .contact-box h2 { position: absolute; left: 71px; top: 40px; font-family: "Raleway", sans-serif; font-size: 39px; font-weight: 600; color: #111; }
  .contact-info { position: absolute; left: 71px; top: 102px; font-size: 13.5px; line-height: 20px; color: #333; }
  .contact-info p { margin-bottom: 16px; }
  .contact-form { position: absolute; left: 545px; top: 44px; width: 480px; }
  .contact-form .row { display: flex; gap: 12px; margin-bottom: 11px; }
  .contact-form .input { flex: 1; height: 42px; border: 1px solid var(--line); font-size: 13px; color: #999; padding: 10px 12px; }
  .contact-form .textarea { height: 80px; margin-bottom: 11px; }
  .contact-form .send { height: 46px; background: var(--grey-btn); color: var(--white); font-size: 20px; font-weight: 600; display: flex; align-items: center; justify-content: center; }

  /* Footer */
  .site-footer { position: absolute; left: 0; top: 2491px; width: 1200px; height: 427px; background: var(--footer); color: var(--footer-text); }
  .footer-col { position: absolute; top: 60px; }
  .footer-col h4 { color: var(--white); font-size: 14px; font-weight: 700; text-transform: uppercase; letter-spacing: .2px; }
  .footer-col h4::after { content: ""; display: block; width: 46px; height: 3px; background: var(--orange); margin-top: 13px; }
  .footer-col p { margin-top: 30px; font-size: 13px; line-height: 24px; }
  .footer-col ul { list-style: none; margin-top: 28px; }
  .footer-col li { font-size: 12.5px; line-height: 31.5px; }
  .footer-col li::before { content: "›"; margin-right: 9px; color: #aaa; }
  .subscribe { margin-top: 24px; width: 252px; height: 36px; background: #1e1e1e; display: flex; align-items: center; justify-content: space-between; padding: 0 14px; font-size: 12px; color: #999; }
  .footer-rule { position: absolute; left: 340px; top: 325px; width: 790px; height: 1px; background: #3d3d3d; }
  .footer-meta { position: absolute; top: 355px; }
  .footer-meta .label { font-size: 12.5px; color: var(--orange); display: flex; align-items: center; gap: 6px; }
  .footer-meta .value { font-size: 17px; color: #ddd; margin-top: 4px; }
  .copyright { position: absolute; left: 0; top: 2918px; width: 1200px; height: 43px; background: var(--footer-bottom); color: #999; font-size: 12px; text-align: center; line-height: 43px; }
</style>
</head>
<body>

<header class="site-header">
  <div class="abs brand"><span>Portalia720º</span><span class="brand-mark"></span></div>
  <div class="abs top-mail">
    <svg width="18" height="13" viewBox="0 0 18 13"><rect x="0.5" y="0.5" width="17" height="12" fill="#555"/><path d="M1 1 L9 7 L17 1" stroke="#fff" stroke-width="1.4" fill="none"/></svg>
    info@portalia720.example
  </div>
  <div class="abs top-phone">
    <svg width="14" height="14" viewBox="0 0 24 24"><path fill="#fff" d="M6.6 10.8a15.1 15.1 0 0 0 6.6 6.6l2.2-2.2c.3-.3.7-.4 1-.2 1.1.4 2.3.6 3.6.6.6 0 1 .4 1 1V20c0 .6-.4 1-1 1A17 17 0 0 1 3 4c0-.6.4-1 1-1h3.5c.6 0 1 .4 1 1 0 1.3.2 2.5.6 3.6.1.3 0 .7-.2 1z"/></svg>
    555 555 5555
  </div>
  <div class="abs social one"></div>
  <div class="abs social two"></div>
  <nav class="abs main-nav">
    <a class="active">HOME</a><a>ABOUT US</a><a>CONTACT</a><a>SERVICES</a><a>EMPLOYMENT</a><a>REVIEWS</a>
  </nav>
</header>

<section class="hero">
  <div class="hero-photo" role="img" aria-label="City skyline of tall towers under a pale hazy sky"></div>
  <div class="estimate-band">
    <h2>We offer what you can afford</h2>
    <div class="estimate-form">
      <svg class="search-icon" viewBox="0 0 50 50"><circle cx="21" cy="21" r="14" fill="none" stroke="#fff" stroke-width="5"/><line x1="31" y1="31" x2="45" y2="45" stroke="#fff" stroke-width="6" stroke-linecap="round"/></svg>
      <div class="field" style="width:148px">Post code</div>
      <div class="field" style="width:128px">No. of homes</div>
      <div class="field" style="width:128px">No. of garages</div>
      <div class="field" style="width:110px">No. of stores</div>
      <div class="field" style="width:190px">Swimming pool (yes/no)</div>
      <div class="field" style="width:154px">Concierge (yes/no)</div>
      <div class="submit">Submit</div>
    </div>
  </div>
</section>

<h1 class="abs provide-title">WE PROVIDE YOU</h1>
<p class="abs provide-lead">Deciding what to take with you is a very personal choice. We provide tools and guidance as well as hands on sorting assistance tailored to your needs and addressing your concerns.</p>

<article class="abs service-card" style="left:61px">
  <h3>Administration</h3>
  <div class="service-photo" role="img" aria-label="Colourful multi-storey apartment building" style="background:linear-gradient(180deg,#e9eef2 0%,#e8d7a8 45%,#c8473f 75%,#6a6a5e 100%)"></div>
  <p>We cover the entire United States as well as servicing relocations within the state of Arizona. Additionally, if you require services for any international move, within or outside the continental United States.</p>
  <div class="card-btn">Contact us or Read More <svg width="8" height="12" viewBox="0 0 8 12"><path d="M1 1l5 5-5 5" stroke="#fff" stroke-width="2" fill="none"/></svg></div>
</article>
<article class="abs service-card" style="left:454px">
  <h3>Consulting</h3>
  <div class="service-photo" role="img" aria-label="Modern two-storey house with lawn under blue sky" style="background:linear-gradient(180deg,#9cbfe0 0%,#c9d6e0 40%,#a98a6c 65%,#5e7a3e 100%)"></div>
  <p>We cover the entire United States as well as servicing relocations within the state of Arizona. Additionally, if you require services for any international move, within or outside the continental United States.</p>
  <div class="card-btn">Contact us or Read More <svg width="8" height="12" viewBox="0 0 8 12"><path d="M1 1l5 5-5 5" stroke="#fff" stroke-width="2" fill="none"/></svg></div>
</article>
<article class="abs service-card" style="left:845px">
  <h3>Mediation</h3>
  <div class="service-photo" role="img" aria-label="Clients reviewing building plans with a contractor" style="background:linear-gradient(180deg,#e6e6e6 0%,#c9a897 45%,#5a7fb5 80%,#3c5a8a 100%)"></div>
  <p>We cover the entire United States as well as servicing relocations within the state of Arizona. Additionally, if you require services for any international move, within or outside the continental United States.</p>
  <div class="card-btn">Contact us or Read More <svg width="8" height="12" viewBox="0 0 8 12"><path d="M1 1l5 5-5 5" stroke="#fff" stroke-width="2" fill="none"/></svg></div>
</article>

<section class="news">
  <h2>Portalia720º International Group Limited Completes Asset Acquisition of Technologies Inc</h2>
  <div class="tablet" role="img" aria-label="Hands holding a tablet showing a video of a suburban house" style="background:linear-gradient(180deg,#f3f3f3 0%,#e8e8e8 12%,#7a9cc4 30%,#8a6a55 62%,#5c6e3c 100%);border-radius:24px 24px 0 0"></div>
  <svg class="abs" style="left:354px;top:324px" width="78" height="78" viewBox="0 0 78 78"><circle cx="39" cy="39" r="36" fill="#fff"/><circle cx="39" cy="39" r="31" fill="#e1261c"/><path d="M31 24 L56 39 L31 54 Z" fill="#fff"/></svg>
  <p class="news-copy">We shipped over 1 million of our Keystone Leases and HarborKeys since 2003. There have been no adverse reactions reported to date. But no news is not as strong as good news. We are proud of the stories that are shared with us on a daily basis on how our products save lives, make medical professionals' jobs easier and how we have made patient care stronger.We shipped over 1 million of our Keystone Leases and HarborKeys since 2003. There have been no adverse reactions reported to date.</p>
  <div class="news-btn">Share Your Success Story</div>
</section>

<section class="contact">
  <div class="contact-box">
    <h2>CONTACT US</h2>
    <div class="contact-info">
      <p>418 Calle Ferrolana, Suite 12<br>Madrid 28014 Spain</p>
      <p>Telephone: +34 910 555 214<br>Toll Free: 900 555 318</p>
      <p>Customer Solutions Phone Extension: x300<br>Customer Solutions Fax: +34 910 555 400<br>Main Fax: +34 910 555 401<br>Email: hello@portalia720.example</p>
    </div>
    <div class="contact-form">
      <div class="row"><div class="input">Your Name</div><div class="input">Your Email</div></div>
      <div class="row"><div class="input">Phone</div><div class="input">Pin Code</div></div>
      <div class="input textarea">Other Details</div>
      <div class="send">Submit</div>
    </div>
  </div>
</section>

<footer class="site-footer">
  <div class="footer-col" style="left:75px;width:250px">
    <h4>About Portalia Estates</h4>
    <p>Phasellus at quam tristique, cursus tellus vitae, convallis neque. Sed a lacinia sapien. Etiam dignissim sit amet felis ac sagittis. Sed libero arcu, pharetra et ante in elementum.</p>
  </div>
  <div class="footer-col" style="left:366px">
    <h4>Useful Links</h4>
    <ul><li>Privacy Policy</li><li>Terms of Services</li><li>Surgery &amp; Transplant Guide</li><li>Special Services</li><li>Sitemap</li></ul>
  </div>
  <div class="footer-col" style="left:622px">
    <h4>Quick Links</h4>
    <ul><li>About Us</li><li>Company History</li><li>Supply Medicine Management</li><li>Doctor's Information Checking</li><li>Doctor's Forum</li><li>News</li></ul>
  </div>
  <div class="footer-col" style="left:856px;width:290px">
    <h4>Newsletter Subscribe</h4>
    <p>Vivamus consequat, felis at aliquam elementum, massa sem dignissim elit, sit amet cursus massa tortor eget ante.</p>
    <div class="subscribe">Enter your email here... <svg width="18" height="12" viewBox="0 0 18 12"><path d="M0 6h15M10 1l6 5-6 5" stroke="#ef7d0a" stroke-width="2" fill="none"/></svg></div>
  </div>
  <div class="footer-rule"></div>
  <div class="footer-meta" style="left:340px">
    <div class="label"><svg width="13" height="13" viewBox="0 0 24 24"><path fill="#ef7d0a" d="M6.6 10.8a15.1 15.1 0 0 0 6.6 6.6l2.2-2.2c.3-.3.7-.4 1-.2 1.1.4 2.3.6 3.6.6.6 0 1 .4 1 1V20c0 .6-.4 1-1 1A17 17 0 0 1 3 4c0-.6.4-1 1-1h3.5c.6 0 1 .4 1 1 0 1.3.2 2.5.6 3.6.1.3 0 .7-.2 1z"/></svg>Call Us Anytime</div>
    <div class="value">(+034)-555-61720</div>
  </div>
  <div class="footer-meta" style="left:528px">
    <div class="label"><svg width="13" height="13" viewBox="0 0 14 14"><circle cx="7" cy="7" r="6" fill="none" stroke="#ef7d0a" stroke-width="1.6"/><path d="M7 3v4h3" stroke="#ef7d0a" stroke-width="1.6" fill="none"/></svg>Opening Hours</div>
    <div class="value">8:00 am - 6:00 pm</div>
  </div>
  <div class="footer-meta" style="left:718px">
    <div class="label"><svg width="14" height="10" viewBox="0 0 14 10"><rect width="14" height="10" fill="#ef7d0a"/><path d="M1 1l6 5 6-5" stroke="#2b2b2b" stroke-width="1.2" fill="none"/></svg>Email Us At</div>
    <div class="value">care@portalia720.example</div>
  </div>
</footer>
<div class="copyright">© 2016 Copyright Portalia720º  All Right Reserved.</div>

</body>
</html>
```